Website Re-design for Kids Playhouse Business

Need current website which looks very outdated to be re-designed to look modern and contemporary, reduce clutter significantly and make it look elegant and simple.
Current website: http://www.tamblewood.com.au/
A website which the business owner likes, use as reference/inspiration: http://rivesta.com.au/
Looking for light green palette, natural colours. "WHAT'S ON" page/link no longer required.
Updates
Industry/Entity Type
Business
Number of Pages Required
5+ page
Look and feel

```html
<!DOCTYPE html>
<html lang="en">
<head>
<meta charset="utf-8">
<title>Tamblewood Kids Playhouse &amp; Cafe</title>
<link rel="stylesheet" href="https://fonts.googleapis.com/css2?family=Montserrat:wght@400;500;600;700&family=Open+Sans:ital,wght@0,400;0,600;1,400&display=swap">
<style>
:root{
  --green:#5cbb2c;
  --green-deep:#3f9f2a;
  --green-light:#86d845;
  --green-pale:#eef6e6;
  --orange:#f9a71c;
  --orange-deep:#f39312;
  --ink:#1f1f1f;
  --text:#555;
  --white:#fff;
}
html,body{margin:0;padding:0;overflow:hidden;}
body{width:1200px;height:3072px;background:var(--white);font-family:"Open Sans",Arial,sans-serif;color:var(--text);}
.page{position:relative;width:1200px;height:3072px;overflow:hidden;}
.abs{position:absolute;}
h1,h2,h3{font-family:"Montserrat",Arial,sans-serif;font-weight:500;margin:0;}

/* hero */
.hero-photo{left:0;top:0;width:1200px;height:682px;background:linear-gradient(135deg,#f3eadf 0%,#e9d6e2 30%,#f0c9d4 55%,#dfe7f2 75%,#c9b7d6 100%);}
.brand{left:118px;top:76px;display:flex;align-items:center;gap:10px;white-space:nowrap;}
.brand-mark{width:18px;height:18px;border-radius:50%;background:var(--green);}
.brand-name{font-family:"Montserrat",Arial,sans-serif;font-weight:600;font-size:28px;line-height:32px;color:var(--green);}
.menu{left:1018px;top:48px;width:46px;}
.menu span{display:block;height:4px;background:#666;border-radius:2px;margin-bottom:8px;}
.welcome{left:82px;top:218px;width:362px;height:362px;border-radius:50%;background:var(--green);border:8px solid var(--white);box-shadow:0 0 0 5px var(--green-light);text-align:center;color:var(--white);box-sizing:border-box;}
.welcome .pre{font-family:"Montserrat",Arial,sans-serif;font-size:19px;margin-top:84px;}
.welcome h1{font-size:30px;line-height:36px;margin-top:6px;}
.welcome p{font-size:12px;line-height:18px;margin:14px 60px 0;}
.dots{margin-top:20px;}
.dots i{display:inline-block;width:12px;height:12px;border-radius:50%;background:var(--white);margin:0 4px;}
.dots i.off{background:transparent;border:2px solid var(--white);box-sizing:border-box;}

/* about */
.about-photo{left:126px;top:696px;width:340px;height:390px;border-radius:40% 40% 10px 10px;background:radial-gradient(circle at 50% 45%,#f6d5c6 0%,#f0a8b5 45%,#f5f5f5 80%);}
.about{left:614px;top:752px;width:480px;}
.about h2{font-size:33px;line-height:36px;color:var(--ink);}
.about p{font-size:13px;line-height:24px;margin:16px 0 0;}
.btn-outline{display:inline-block;margin-top:28px;width:160px;height:52px;line-height:48px;border:2px solid var(--green);border-radius:26px;text-align:center;color:var(--green);font-family:"Montserrat",Arial,sans-serif;font-size:16px;font-weight:500;box-sizing:border-box;}

/* features */
.features-bg{left:0;top:1040px;}
.section-title{width:1200px;left:0;text-align:center;font-size:33px;}
.section-title::after{content:"";display:block;width:76px;height:4px;margin:10px auto 0;border-radius:2px;background:var(--green);}
.features-title{top:1178px;color:var(--white);}
.features-title::after{background:var(--white);}
.feature{top:1250px;width:280px;text-align:center;color:var(--white);}
.feature-ring{width:276px;height:276px;border-radius:50%;border:2px dashed var(--white);box-sizing:border-box;padding:12px;margin:0 auto;}
.feature-photo{width:248px;height:248px;border-radius:50%;}
.feature h3{font-family:"Open Sans",Arial,sans-serif;font-weight:400;font-size:20px;line-height:25px;margin-top:14px;}
.btn-small{display:inline-block;margin-top:12px;width:136px;height:42px;line-height:38px;border:2px solid var(--white);border-radius:21px;font-size:14px;font-family:"Montserrat",Arial,sans-serif;box-sizing:border-box;}
.arrow{width:50px;height:50px;}

/* testimonials */
.testi-title{top:1760px;color:var(--ink);}
.quote{left:210px;top:1868px;width:714px;height:225px;border:2px solid var(--green);border-radius:112px;background:var(--white);box-sizing:border-box;text-align:center;}
.quote p{font-style:italic;font-size:16px;line-height:29px;margin:48px 58px 0;color:#666;}
.quote .author{font-style:normal;font-size:16px;color:var(--ink);margin-top:18px;}
.quote-badge{left:564px;top:1842px;width:52px;height:52px;}

/* contact */
.contact-title{top:2218px;color:var(--ink);}
.form-box{left:166px;top:2292px;width:864px;height:310px;border:2px solid var(--green);border-radius:40px;background:var(--white);box-sizing:border-box;}
.field{height:42px;border:1px solid #cfcfcf;border-radius:3px;font-size:13px;color:#444;padding:12px 14px;box-sizing:border-box;}
.btn-solid{left:526px;top:2570px;width:156px;height:48px;line-height:48px;border-radius:24px;background:var(--green);color:var(--white);text-align:center;font-family:"Montserrat",Arial,sans-serif;font-size:18px;font-weight:500;}
.toy-photo{left:30px;top:2412px;width:140px;height:172px;background:linear-gradient(180deg,#e8463a 0%,#f5c52b 40%,#37a84b 65%,#3b7fd1 100%);border-radius:50% 50% 12px 12px;}
.child-photo{left:1016px;top:2320px;width:156px;height:220px;border-radius:70px 70px 20px 20px;background:linear-gradient(180deg,#f4d9bf 0%,#f1c6a7 50%,#d93f3f 100%);}

/* footer */
.footer-bg{left:0;top:2632px;}
.footer-col{top:2748px;color:var(--white);}
.footer-col h3{font-size:20px;font-weight:400;margin-bottom:14px;}
.footer-col ul{list-style:none;margin:0;padding:0;}
.footer-col li{font-size:14px;line-height:27px;}
.footer-col svg{vertical-align:-3px;margin-right:10px;}
.social{display:flex;gap:6px;}
.social span{width:38px;height:38px;border:2px solid var(--white);border-radius:50%;box-sizing:border-box;}
.copyright{left:0;top:3005px;width:1200px;height:67px;line-height:67px;background:var(--orange-deep);text-align:center;color:var(--white);font-size:13px;}
</style>
</head>
<body>
<div class="page">

  <!-- hero -->
  <div class="abs hero-photo" role="img" aria-label="Photo of two toddlers playing with a toy tea set in a bright playroom"></div>
  <div class="abs brand">
    <span class="brand-mark"></span>
    <span class="brand-name">Tamblewood Kids</span>
  </div>
  <div class="abs menu"><span></span><span></span><span></span></div>
  <div class="abs welcome">
    <div class="pre">Welcome to</div>
    <h1>Tamblewood Kids<br>Playhouse &amp; Cafe</h1>
    <p>Etiam eu urna Sed porta Suspendisse quam leo molestie sed luctus</p>
    <div class="dots"><i class="off"></i><i></i><i></i><i></i></div>
  </div>

  <!-- about -->
  <div class="abs about-photo" role="img" aria-label="Photo of a toddler building with colourful blocks"></div>
  <div class="abs about">
    <h2>About Tamblewood Kids<br>Playhouse &amp; Cafe</h2>
    <p>Fusce ultricies orci ac feugiat suscipit leo massa sodales velit et scelerisque mi tortor at ipsum cligula augue bibendum accumsan</p>
    <p style="margin-top:10px">malesuada iaculis ipsum dui aliquet felis at cursus magna nisl nec elit Praesent elementum elit at tellus nec ultricies sit amet porttitor mattis enim In massa libero interdum nec interdum vel blandit sed</p>
    <span class="btn-outline">Read More</span>
  </div>

  <!-- features -->
  <svg class="abs features-bg" width="1200" height="700" viewBox="0 0 1200 700" aria-hidden="true">
    <defs>
      <linearGradient id="featureGreen" x1="0" y1="0" x2="1" y2="0">
        <stop offset="0" stop-color="#4caf24"/><stop offset="1" stop-color="#7cd43e"/>
      </linearGradient>
    </defs>
    <path d="M700 80 C900 90 1080 40 1200 0 L1200 40 C1080 80 900 120 700 80Z" fill="#b8e28f"/>
    <path d="M0 66 C250 40 520 110 780 100 C960 92 1090 50 1200 22 L1200 690 C1000 660 800 650 600 656 C380 662 180 700 0 720Z" fill="url(#featureGreen)"/>
  </svg>
  <h2 class="abs section-title features-title">Our Features</h2>

  <svg class="abs arrow" style="left:57px;top:1422px" viewBox="0 0 50 50" aria-hidden="true"><circle cx="25" cy="25" r="23" fill="none" stroke="#fff" stroke-width="2"/><path d="M29 15 L19 25 L29 35" fill="none" stroke="#fff" stroke-width="3" stroke-linecap="round" stroke-linejoin="round"/></svg>
  <svg class="abs arrow" style="left:1098px;top:1422px" viewBox="0 0 50 50" aria-hidden="true"><circle cx="25" cy="25" r="23" fill="none" stroke="#fff" stroke-width="2"/><path d="M21 15 L31 25 L21 35" fill="none" stroke="#fff" stroke-width="3" stroke-linecap="round" stroke-linejoin="round"/></svg>

  <div class="abs feature" style="left:138px">
    <div class="feature-ring"><div class="feature-photo" role="img" aria-label="Photo of girls dancing at a birthday party" style="background:radial-gradient(circle,#f7d7cb 0%,#e78fa4 60%,#c65d7a 100%)"></div></div>
    <h3>Perfect venue for<br>birthdays &amp; private parties</h3>
    <span class="btn-small">Read More</span>
  </div>
  <div class="abs feature" style="left:464px">
    <div class="feature-ring"><div class="feature-photo" role="img" aria-label="Photo of a child in a colourful ball pit" style="background:radial-gradient(circle,#f4e26a 0%,#e45a4a 40%,#3d7fd0 75%,#2e9b4d 100%)"></div></div>
    <h3>4 kids loving<br>party rooms themes</h3>
    <span class="btn-small">Read More</span>
  </div>
  <div class="abs feature" style="left:798px">
    <div class="feature-ring"><div class="feature-photo" role="img" aria-label="Photo of wooden toy blocks in a sunny classroom" style="background:radial-gradient(circle,#fbf8f0 0%,#e8dccb 55%,#c9b190 100%)"></div></div>
    <h3>We host school<br>holiday programs</h3>
    <span class="btn-small">Read More</span>
  </div>

  <!-- testimonials -->
  <div class="abs" role="img" aria-label="Faint pattern of toy and playroom doodles" style="left:0;top:1700px;width:1200px;height:472px;background:linear-gradient(180deg,#f1f8ea 0%,#e7f2dc 100%);z-index:-1"></div>
  <h2 class="abs section-title testi-title">Testimonials</h2>
  <svg class="abs arrow" style="left:136px;top:1952px" viewBox="0 0 50 50" aria-hidden="true"><circle cx="25" cy="25" r="23" fill="#fff" stroke="#5cbb2c" stroke-width="2"/><path d="M29 15 L19 25 L29 35" fill="none" stroke="#5cbb2c" stroke-width="3" stroke-linecap="round" stroke-linejoin="round"/></svg>
  <svg class="abs arrow" style="left:993px;top:1952px" viewBox="0 0 50 50" aria-hidden="true"><circle cx="25" cy="25" r="23" fill="#fff" stroke="#5cbb2c" stroke-width="2"/><path d="M21 15 L31 25 L21 35" fill="none" stroke="#5cbb2c" stroke-width="3" stroke-linecap="round" stroke-linejoin="round"/></svg>
  <div class="abs quote">
    <p>Excellent place for kids and parents, amazing party rooms, friendly, fun and helpful staff! I highly recommend for hosting your next party or just to relax in air-con whilst watching your kids have a ball on the play equipment and activities!</p>
    <div class="author">By Author Name</div>
  </div>
  <svg class="abs quote-badge" viewBox="0 0 52 52" aria-hidden="true"><circle cx="26" cy="26" r="26" fill="#5cbb2c"/><path d="M14 34 V27 C14 21 17 18 22 17 L22 20 C19 21 18 23 18 25 H23 V34Z M29 34 V27 C29 21 32 18 37 17 L37 20 C34 21 33 23 33 25 H38 V34Z" fill="#fff"/></svg>

  <!-- contact -->
  <h2 class="abs section-title contact-title">Contact Us</h2>
  <div class="abs toy-photo" role="img" aria-label="Photo of a stacking ring toy and a toy car"></div>
  <div class="abs child-photo" role="img" aria-label="Photo of a smiling toddler peeking around the form"></div>
  <div class="abs form-box"></div>
  <div class="abs field" style="left:203px;top:2330px;width:390px">Name</div>
  <div class="abs field" style="left:604px;top:2330px;width:392px">Email address</div>
  <div class="abs field" style="left:203px;top:2382px;width:390px">Phone</div>
  <div class="abs field" style="left:604px;top:2382px;width:392px">Postcode</div>
  <div class="abs field" style="left:203px;top:2436px;width:793px;height:100px">Message</div>
  <div class="abs btn-solid">Submit</div>

  <!-- footer -->
  <svg class="abs footer-bg" width="1200" height="380" viewBox="0 0 1200 380" aria-hidden="true">
    <path d="M0 20 C300 70 700 70 1200 0 L1200 20 C700 90 300 90 0 40Z" fill="#fcd58a"/>
    <path d="M0 40 C300 90 700 90 1200 20 L1200 380 L0 380Z" fill="#f9a71c"/>
  </svg>
  <div class="abs footer-col" style="left:128px">
    <h3>Quick Links</h3>
    <ul><li>Home</li><li>Hours &amp; Prices</li><li>Party Packages</li><li>Party Rooms</li></ul>
  </div>
  <div class="abs footer-col" style="left:368px">
    <h3>Resources</h3>
    <ul><li>Vacation Care</li><li>School Holiday Program</li><li>Specials &amp; Promotions</li><li>Gallery</li><li>Contact</li></ul>
  </div>
  <div class="abs footer-col" style="left:628px">
    <h3>Contact Us</h3>
    <ul>
      <li><svg width="14" height="16" viewBox="0 0 14 16"><path d="M7 0 C3 0 1 3 1 6 C1 10 7 16 7 16 C7 16 13 10 13 6 C13 3 11 0 7 0Z" fill="#fff"/><circle cx="7" cy="6" r="2.2" fill="#f9a71c"/></svg>14 Fernbrook Lane Marlow</li>
      <li style="padding-left:24px">2290 NSW Australia</li>
      <li><svg width="14" height="14" viewBox="0 0 14 14"><path d="M3 0 L5.5 3.5 L4 5.5 C5 7.5 6.5 9 8.5 10 L10.5 8.5 L14 11 L12 14 C6 13.5 0.5 8 0 2Z" fill="#fff"/></svg>02 5550 0140</li>
      <li><svg width="14" height="14" viewBox="0 0 14 14"><rect x="3" y="0" width="8" height="4" fill="#fff"/><rect x="0" y="5" width="14" height="6" rx="1" fill="#fff"/><rect x="3" y="9" width="8" height="5" fill="#fff" stroke="#f9a71c"/></svg>02 5550 0141</li>
      <li><svg width="14" height="12" viewBox="0 0 14 12"><rect x="0" y="1" width="14" height="10" rx="1" fill="#fff"/><path d="M0.5 1.5 L7 6.5 L13.5 1.5" fill="none" stroke="#f9a71c" stroke-width="1.4"/></svg>hello@tamblewoodplay.com</li>
    </ul>
  </div>
  <div class="abs footer-col" style="left:905px">
    <h3>Follow Us</h3>
    <div class="social" aria-label="Social media links"><span></span><span></span><span></span><span></span></div>
  </div>
  <div class="abs copyright">© 2018 Company Name &nbsp;All right reserved</div>

</div>
</body>
</html>
```